Kleine Website f. Unternehmensdarstellung
Zielgruppe
Geschäftsführer, Marketing & Sales Manager asiatischer Konzerne.
Aufgabenstellung
Wir sind eine Consulting und Handelsagentur mit überwiegend internationaler Kundschaft (Asien 70%).
Für einen Webauftritt, ca. 8 Seiten, haben wir eine Powerpoint Vorlage erstellt, diese zeigt nur die Inhalte. Wir benötigen nun daraus eine Website, haben eigenen Webspace, eigener Server bei Servantik. Wir stellen uns als Hintergrundbild auf der Frontpage Hongkong vor. Keine Flash videos oder audio einbindung ! Sprache Englisch, die Texte sollten von uns leicht editierbar sein, falls mal Anpassungen gemacht werden müssen.

```html
<!DOCTYPE html>
<html lang="en">
<head>
<meta charset="utf-8">
<title>Veldaro Group</title>
<link rel="stylesheet" href="https://fonts.googleapis.com/css2?family=Arimo:wght@400;700&display=swap">
<style>
:root{
  --page-top:#3b5fb8;
  --page-mid:#6b8fe0;
  --page-low:#4a62c4;
  --night:#0c1230;
  --panel:rgba(110,145,230,.55);
  --panel-edge:rgba(190,210,255,.35);
  --tab-dark:#2a1a8a;
  --tab-light:#9a7df0;
  --text:#ffffff;
  --text-soft:#e4ebff;
  --nav-active:#2b1580;
}
*{box-sizing:border-box;margin:0;padding:0}
html,body{width:1007px;height:1200px;overflow:hidden}
body{font-family:"Arimo",Arial,sans-serif;color:var(--text);background:#fff}
.page{position:relative;width:1007px;height:1200px;overflow:hidden;
  background:linear-gradient(180deg,var(--page-top) 0%,var(--page-mid) 35%,var(--page-mid) 55%,var(--page-low) 68%,var(--night) 100%)}
.skyline-photo{position:absolute;left:0;right:0;bottom:0;height:420px;
  background:
    radial-gradient(ellipse at 30% 70%,rgba(255,200,230,.35),transparent 45%),
    radial-gradient(ellipse at 75% 60%,rgba(180,210,255,.35),transparent 40%),
    linear-gradient(180deg,rgba(60,80,170,0) 0%,#2a2f6a 35%,#151a3d 70%,#0a0d24 100%)}
.brand{position:absolute;left:35px;top:50px;display:flex;align-items:center;gap:12px}
.brand-mark{width:26px;height:26px;background:var(--text)}
.brand-name{font-size:32px;font-weight:700;letter-spacing:4px}
.welcome{position:absolute;left:508px;top:52px}
.welcome h1{font-size:17px;font-weight:400;letter-spacing:.3px}
.welcome p{font-size:10.5px;line-height:14px;margin-left:3px;margin-top:3px;color:var(--text-soft)}
.lang-switch{position:absolute;left:880px;top:0;width:90px;height:78px;
  background:rgba(255,255,255,.12);border-radius:0 0 4px 4px;display:flex;align-items:flex-end;justify-content:center;padding-bottom:14px;gap:0;font-size:13px}
.lang-switch span{padding:0 12px}
.lang-switch span+span{border-left:1px solid rgba(255,255,255,.5)}
.main-nav{position:absolute;left:30px;top:164px;list-style:none}
.main-nav li{font-size:13.5px;font-weight:700;text-decoration:underline;line-height:32px;padding-left:14px;position:relative}
.main-nav li::before{content:"";position:absolute;left:0;top:14px;width:4px;height:4px;border-radius:50%;background:var(--text)}
.main-nav li.active{color:var(--nav-active);text-decoration:none}
.world-map{position:absolute;left:42px;top:410px;width:250px;height:145px;border-radius:40px;
  background:radial-gradient(ellipse,rgba(230,238,255,.85),rgba(200,215,255,.4) 60%,transparent 75%)}
.world-clocks{position:absolute;left:40px;top:572px;display:flex;gap:26px}
.clock{width:44px;text-align:center}
.clock svg{display:block}
.clock-label{margin-top:9px;font-size:7px;color:#334;background:rgba(235,240,255,.85);padding:1px 2px}
.panels{position:absolute;left:335px;top:155px;display:grid;grid-template-columns:312px 313px;grid-template-rows:245px 245px 245px;gap:11px}
.panel{background:var(--panel);border:1px solid var(--panel-edge);border-radius:4px;padding:18px 20px 0 53px;font-size:11.5px;line-height:14px}
.panel-tab{width:196px;height:29px;margin-bottom:11px;display:flex;align-items:center;justify-content:center;
  font-size:11.5px;font-weight:700;letter-spacing:.4px;border:1px solid rgba(255,255,255,.7);
  background:linear-gradient(90deg,var(--tab-light) 0%,#5a3ad0 30%,var(--tab-dark) 100%)}
.panel-tab.news{background:linear-gradient(90deg,#c8d4ff 0%,#5e73c8 40%,#1d2466 100%)}
.panel ul{list-style:none}
.panel li{position:relative;padding-left:12px;margin-bottom:5px}
.panel li::before{content:"•";position:absolute;left:0}
.panel p+p{margin-top:0}
.more{display:block;margin-top:2px;margin-left:2px}
.more::before{content:"→";margin-right:12px}
.more span{text-decoration:underline}
.gap{margin-top:14px}
.news-date{font-size:14px;font-weight:700;margin-top:2px}
.news-item+.news-item{margin-top:16px}
.news-item p{text-align:justify;width:205px}
.presentation{display:flex;align-items:center;justify-content:center;gap:14px;padding:0}
.pdf-badge{width:56px;height:56px;border-radius:50%;background:radial-gradient(circle at 40% 35%,#3a4fb8,#0d1560 70%);
  border:2px solid #cdd8ff;display:flex;flex-direction:column;align-items:center;justify-content:center;font-weight:700;font-size:15px;line-height:13px}
.pdf-badge small{font-size:6px;font-weight:400}
.presentation-title{font-size:22px;line-height:20px}
.presentation-title small{display:block;font-size:12.5px;letter-spacing:1px;text-align:center}
.footer-note{position:absolute;right:32px;bottom:8px;font-size:13px;color:var(--text-soft);display:flex;align-items:center;gap:8px}
.footer-note i{width:10px;height:10px;background:var(--text-soft);display:block}
</style>
</head>
<body>
<div class="page">
  <div class="skyline-photo" role="img" aria-label="Night skyline of Hong Kong with glowing towers"></div>

  <div class="brand"><div class="brand-mark"></div><span class="brand-name">VELDARO</span></div>

  <div class="welcome">
    <h1>WELCOME TO THE VELDARO GROUP</h1>
    <p>OUR BUSINESS SEGMENTS COVER QUITE AN AREA,<br>PLEASE SELECT YOUR PIONT OF INTEREST.</p>
  </div>

  <div class="lang-switch"><span>EN</span><span>DE</span></div>

  <ul class="main-nav">
    <li class="active">HOME</li>
    <li>OPTOELECTRONICS / SEMICONDUCTORS</li>
    <li>TECHNOLOGY FINANCE</li>
    <li>TROUBLE SHOOTING</li>
    <li>M &amp; A THE SILENT SERVICE</li>
  </ul>

  <div class="world-map" role="img" aria-label="Glowing world map"></div>

  <div class="world-clocks">
    <div class="clock"><svg width="44" height="44" viewBox="0 0 44 44"><circle cx="22" cy="22" r="20" fill="#eef2ff" stroke="#8a9bd0" stroke-width="2"/><line x1="22" y1="22" x2="22" y2="8" stroke="#223" stroke-width="1.5"/><line x1="22" y1="22" x2="30" y2="26" stroke="#223" stroke-width="1.5"/></svg><div class="clock-label">New York</div></div>
    <div class="clock"><svg width="44" height="44" viewBox="0 0 44 44"><circle cx="22" cy="22" r="20" fill="#eef2ff" stroke="#8a9bd0" stroke-width="2"/><line x1="22" y1="22" x2="22" y2="8" stroke="#223" stroke-width="1.5"/><line x1="22" y1="22" x2="32" y2="22" stroke="#223" stroke-width="1.5"/></svg><div class="clock-label">London</div></div>
    <div class="clock"><svg width="44" height="44" viewBox="0 0 44 44"><circle cx="22" cy="22" r="20" fill="#eef2ff" stroke="#8a9bd0" stroke-width="2"/><line x1="22" y1="22" x2="22" y2="8" stroke="#223" stroke-width="1.5"/><line x1="22" y1="22" x2="28" y2="32" stroke="#223" stroke-width="1.5"/></svg><div class="clock-label">Moscow</div></div>
    <div class="clock"><svg width="44" height="44" viewBox="0 0 44 44"><circle cx="22" cy="22" r="20" fill="#eef2ff" stroke="#8a9bd0" stroke-width="2"/><line x1="22" y1="22" x2="22" y2="8" stroke="#223" stroke-width="1.5"/><line x1="22" y1="22" x2="14" y2="30" stroke="#223" stroke-width="1.5"/></svg><div class="clock-label">Hongkong</div></div>
  </div>

  <div class="panels">
    <section class="panel">
      <div class="panel-tab">OPTOELECTRONICS</div>
      <p>We offer an outstanding service to our customers. Based on our 30 years market experience, we have unrivaled skillsets to increase our customers sales volume.<br>We differentiate between Consultancy and Agency business models.</p>
      <a class="more"><span>more</span></a>
    </section>
    <section class="panel">
      <div class="panel-tab">TROUBLE SHOOTING</div>
      <ul>
        <li>Your project runs out of bounds ?</li>
        <li>Pricing, quality and milestones are not metby the vendors ?</li>
        <li>Prototype works but the transition to industrial usage stucks ?</li>
        <li>You desparately need a second source for mission critical parts ?</li>
      </ul>
      <p class="gap">We are looking for trouble, with us, you will have a proven trouble shooter on your side. We rescued projects worth multi million $.</p>
      <a class="more"><span>more</span></a>
    </section>
    <section class="panel">
      <div class="panel-tab">TECHNOLOGY FINANCING</div>
      <ul>
        <li>You or your company have an outstanding product or idea ?</li>
        <li>For the extension of market shares you need support ?</li>
        <li>You want to retract from Europe and sellyour assets ?</li>
      </ul>
      <p class="gap">This is exactly, what we like and where we can add enormous power.</p>
      <a class="more"><span>more</span></a>
    </section>
    <section class="panel">
      <div class="panel-tab">M &amp; A , THE SILENT SERVICE</div>
      <ul>
        <li>You understand the time to market entrance issue ?</li>
        <li>You want to prove and identify targets for aquisition ?</li>
        <li>You need a proxy to make first contacts and evaluate ?</li>
        <li>You just need a concise market overview about your competitors ?</li>
      </ul>
      <a class="more"><span>more</span></a>
    </section>
    <section class="panel">
      <div class="panel-tab news">NEWS &amp; PRESSE</div>
      <div class="news-item">
        <div class="news-date">28.09.2010</div>
        <p>Ipsum dolor sit amet, consectetuer adipiscing elit. Aenean commodo ligula eget dolor.</p>
        <a class="more"><span>more</span></a>
      </div>
      <div class="news-item">
        <div class="news-date">20.12.2010</div>
        <p>Aenean massa. Cum sociis natoque penatibus et magnis dis parturient montes, nascetur ridiculus mus.</p>
        <a class="more"><span>more</span></a>
      </div>
    </section>
    <section class="panel presentation">
      <div class="pdf-badge">PDF<small>DOWNLOAD</small><small>▼</small></div>
      <div class="presentation-title">COMPANY<small>PRESENTATION</small></div>
    </section>
  </div>

  <div class="footer-note"><i></i>2011 VELDARO</div>
</div>
</body>
</html>
```